Golf Course Hole Sign

I need signs designed for each hole of an 18-hole course.

Each sign will be have a similar design, but different information on each (such as the hole number, yardage, name of the hole, etc.).

Just to be clear, I just need ONE DESIGN. And, then the different course layouts & information can be pasted for each hole, once selected.

The theme of the course is the historical champions of golf, so a historical emphasis would be great. Each hole is named after a golfer.

Sign size: 24-inches wide X 15-inches high.

The sign must contain:
-Hole Number
-Hole Yardage
-Hole layout
-Name of Hole
-Picture of Golfer
-Description?
-Logo of course

I attached a sample to give you an idea of what a sign looks like (but it needs to have all the above information and in the dimension listed above). Also attached, the course layout for the first 6 holes, and the logo.

Target Market(s)

Golfers.

Industry/Entity Type

Golf Course

Requirements
Must have
• Hole layout
Hole Number
Hole Yardage
Name of Hole
Picture of Golfer
Description?
Logo of course

```html
<!DOCTYPE html>
<html lang="en">
<head>
<meta charset="utf-8">
<title>Hole 2 Sign – Heritage Links Club</title>
<link rel="stylesheet" href="https://fonts.googleapis.com/css2?family=Noto+Serif:wght@700;900&display=swap">
<style>
  :root {
    --page-bg: #eef1f3;
    --sign-black: #000000;
    --sign-rim: #a6a6a6;
    --white: #ffffff;
    --label-grey: #bdbdbd;
    --tee-red: #ff1010;
    --tee-white: #ffffff;
    --tee-blue: #3d9de8;
    --tee-yellow: #ffee00;
    --map-rough: #bdbdbd;
    --map-trees: #3f6b34;
    --map-fairway: #6fa85a;
    --map-green: #8cc274;
    --map-fade: #000000;
    --serif: "Noto Serif", Georgia, serif;
  }
  html, body {
    margin: 0;
    padding: 0;
    width: 1200px;
    height: 1116px;
    overflow: hidden;
    background: var(--page-bg);
  }
  .hole-sign {
    position: absolute;
    left: 141px;
    top: 272px;
    width: 918px;
    height: 572px;
    font-family: var(--serif);
    color: var(--white);
  }
  .sign-board {
    position: absolute;
    inset: 0;
  }
  .hole-map {
    position: absolute;
    left: 36px;
    top: 50px;
    width: 272px;
    height: 484px;
    background:
      linear-gradient(90deg,
        var(--map-rough) 0%,
        #9aa894 12%,
        var(--map-trees) 22%,
        #55884a 32%,
        var(--map-fairway) 42%,
        var(--map-green) 50%,
        #4f7d42 60%,
        #2a2a2a 80%,
        var(--map-fade) 100%);
  }
  .golfer-portrait {
    position: absolute;
    left: 302px;
    top: 36px;
    width: 276px;
    height: 156px;
    background: radial-gradient(ellipse 48% 62% at 50% 62%,
      #f2f2f2 0%, #d6d6d6 35%, #6a6a6a 70%, var(--sign-black) 100%);
  }
  .name-rule {
    position: absolute;
    left: 302px;
    width: 276px;
    height: 4px;
    background: var(--white);
  }
  .name-rule--top { top: 192px; }
  .name-rule--bottom { top: 258px; }
  .hole-name {
    position: absolute;
    left: 302px;
    width: 276px;
    top: 198px;
    margin: 0;
    text-align: center;
    font-size: 50px;
    font-weight: 700;
    line-height: 58px;
    letter-spacing: 1px;
  }
  .hole-label {
    position: absolute;
    left: 282px;
    width: 280px;
    top: 270px;
    text-align: center;
    font-size: 42px;
    font-weight: 700;
    color: var(--label-grey);
    line-height: 52px;
  }
  .hole-number {
    position: absolute;
    left: 282px;
    width: 280px;
    top: 302px;
    text-align: center;
    font-size: 200px;
    font-weight: 700;
    line-height: 200px;
  }
  .hole-yardage {
    position: absolute;
    left: 282px;
    width: 280px;
    top: 489px;
    text-align: center;
    font-size: 42px;
    font-weight: 700;
    line-height: 50px;
    letter-spacing: 1px;
  }
  .unit { font-size: 27px; }
  .club-mark {
    position: absolute;
    left: 628px;
    top: 60px;
    width: 200px;
    text-align: center;
  }
  .club-mark__circle {
    width: 112px;
    height: 112px;
    margin: 0 auto 22px;
    border: 4px solid var(--white);
    border-radius: 50%;
    box-sizing: border-box;
  }
  .club-mark__name {
    margin: 0;
    font-size: 16px;
    font-weight: 900;
    line-height: 20px;
  }
  .tee-list {
    position: absolute;
    left: 634px;
    top: 336px;
    margin: 0;
    padding: 0;
    list-style: none;
  }
  .tee {
    display: flex;
    align-items: center;
    height: 50px;
    font-size: 38px;
    font-weight: 700;
  }
  .tee__dot {
    width: 24px;
    height: 24px;
    border-radius: 50%;
    margin-right: 16px;
    flex: none;
  }
  .tee__dot--red { background: var(--tee-red); }
  .tee__dot--white { background: var(--tee-white); }
  .tee__dot--blue { background: var(--tee-blue); }
  .tee__dot--yellow { background: var(--tee-yellow); }
</style>
</head>
<body>
  <section class="hole-sign">
    <svg class="sign-board" width="918" height="572" viewBox="0 0 918 572" aria-hidden="true">
      <polygon points="0,0 820,0 918,286 820,572 0,572" fill="var(--sign-black)"/>
      <polygon points="12,12 812,12 906,286 812,560 12,560" fill="none" stroke="var(--sign-rim)" stroke-width="5"/>
    </svg>

    <div class="hole-map" role="img" aria-label="Aerial layout of hole 2: green at top, fairway with 75, 100, 125, 150 and 175 yard markers, bunkers, tree line on the left and tee boxes at the bottom"></div>

    <div class="golfer-portrait" role="img" aria-label="White silhouette of a golfer at the finish of a swing"></div>

    <div class="name-rule name-rule--top"></div>
    <h1 class="hole-name">ALEX</h1>
    <div class="name-rule name-rule--bottom"></div>

    <div class="hole-label">Hole</div>
    <div class="hole-number">2</div>
    <div class="hole-yardage">75<span class="unit">yds</span></div>

    <div class="club-mark">
      <div class="club-mark__circle"></div>
      <p class="club-mark__name">HERITAGE LINKS<br>CLUB</p>
    </div>

    <ul class="tee-list">
      <li class="tee"><span class="tee__dot tee__dot--red"></span>131<span class="unit">yds</span></li>
      <li class="tee"><span class="tee__dot tee__dot--white"></span>169<span class="unit">yds</span></li>
      <li class="tee"><span class="tee__dot tee__dot--blue"></span>215<span class="unit">yds</span></li>
      <li class="tee"><span class="tee__dot tee__dot--yellow"></span>233<span class="unit">yds</span></li>
    </ul>
  </section>
</body>
</html>
```